Supplement Bottle Packaging and Design

We want to rebrand our current health supplements (see below). We do want it to be modern, vibrant and appealing supplement bottles. Very upscale and elegant as it targets primarily women.
NOTE: READ THE ATTACHED WORD DOCUMENT!
Bottle size: We are totally open to the bottle size and shape, as long it's a typical supplement bottle size to handle 90-120 capsules; what we mostly need is new bottle design/packaging. YOU DON’T HAVE TO USE THE CURRENT WHITE BOTTLE SHAPE, BUT ANYTHING MORE MODERN WOULD WORK!
Updates
We need more modern, clean sleek designs to choose from
Look and feel
Each slider illustrates characteristics of the customer's brand and the style your logo design should communicate.

```html
<!DOCTYPE html>
<html lang="en">
<head>
<meta charset="utf-8">
<title>Align Supplement Labels</title>
<link rel="stylesheet" href="https://fonts.googleapis.com/css2?family=Federo&family=Jost:wght@400;500&display=swap">
<style>
  :root {
    --paper: #ffffff;
    --ink: #1a1a1a;
    --outline: #4a4a4a;
    --sun: #fbf29a;
    --liver: #23104a;
    --liver-mid: #7155a3;
    --tummy: #e00a14;
    --tummy-mid: #f0560f;
    --hormone: #0b5a16;
    --hormone-mid: #64a06a;
    --sugar: #1a6fe0;
    --sugar-mid: #4db0ef;
  }
  * { margin: 0; padding: 0; box-sizing: border-box; }
  html, body { width: 801px; height: 1200px; overflow: hidden; background: var(--paper); }
  .sheet { position: relative; width: 801px; height: 1200px; }
  .label {
    position: absolute; top: 420px; width: 174px; height: 362px;
    --accent: var(--ink); --accent-mid: var(--ink);
  }
  .label--liver { left: 15px; --accent: var(--liver); --accent-mid: var(--liver-mid); }
  .label--tummy { left: 214px; --accent: var(--tummy); --accent-mid: var(--tummy-mid); }
  .label--hormone { left: 413px; --accent: var(--hormone); --accent-mid: var(--hormone-mid); }
  .label--sugar { left: 612px; --accent: var(--sugar); --accent-mid: var(--sugar-mid); }
  .label__cap {
    position: absolute; top: 0; left: 0; width: 100%; height: 59px;
    border: 0.8px solid var(--outline);
  }
  .label__body {
    position: absolute; top: 61px; left: 0; width: 100%; height: 301px;
    border: 0.8px solid var(--outline); border-radius: 0 0 15px 15px;
    overflow: hidden;
  }
  .product-name {
    position: absolute; left: 21px; bottom: 244px; max-width: 142px; white-space: nowrap;
    font-family: "Federo", sans-serif; font-weight: 400; font-size: 26px; line-height: 1;
    color: var(--ink); letter-spacing: -0.4px;
  }
  .label--hormone .product-name { font-size: 21px; }
  .label--sugar .product-name { font-size: 18px; letter-spacing: -0.5px; }
  .rule {
    position: absolute; left: 21px; width: 122px; height: 2px;
    background-image: radial-gradient(circle, var(--accent) 0.9px, transparent 1.1px);
    background-size: 5px 2px; background-repeat: repeat-x;
  }
  .rule--top { top: 65px; }
  .rule--bottom { top: 101px; }
  .claim {
    position: absolute; left: 21px; top: 70px; width: 135px;
    font-family: "Jost", sans-serif; font-size: 11px; line-height: 12.5px;
    color: var(--ink); letter-spacing: 0.2px;
  }
  .badge {
    position: absolute; left: 21px; top: 120px; width: 109px; height: 17px;
    background: var(--accent); color: var(--paper);
    font-family: "Jost", sans-serif; font-size: 11px; line-height: 17px;
    text-align: center; letter-spacing: 0.2px; white-space: nowrap;
  }
  .count {
    position: absolute; left: 21px; top: 187px; display: flex; align-items: center; gap: 2px;
    color: var(--ink);
  }
  .count__number { font-family: "Federo", sans-serif; font-size: 18px; line-height: 1; }
  .count__unit { font-family: "Jost", sans-serif; font-size: 8px; line-height: 8px; }
  .pattern {
    position: absolute; left: 21px; top: 215px; width: 131px; height: 70px;
    background: linear-gradient(180deg, var(--sun) 0%, var(--sun) 28%, var(--accent-mid) 45%, var(--accent) 100%);
  }
</style>
</head>
<body>
<main class="sheet">
  <article class="label label--liver">
    <div class="label__cap"></div>
    <div class="label__body">
      <h2 class="product-name">Liver Align</h2>
      <div class="rule rule--top"></div>
      <p class="claim">Rejuvenating Cleanse<br>&amp; Detox Formula*</p>
      <div class="rule rule--bottom"></div>
      <p class="badge">Dietary Supplement</p>
      <p class="count"><span class="count__number">120</span><span class="count__unit">Vegetable<br>Capsules</span></p>
      <div class="pattern" role="img" aria-label="Band of triangles fading from pale yellow to deep purple"></div>
    </div>
  </article>
  <article class="label label--tummy">
    <div class="label__cap"></div>
    <div class="label__body">
      <h2 class="product-name">Tummy Align</h2>
      <div class="rule rule--top"></div>
      <p class="claim">Oxygenating Colon<br>Cleanse*</p>
      <div class="rule rule--bottom"></div>
      <p class="badge">Dietary Supplement</p>
      <p class="count"><span class="count__number">90</span><span class="count__unit">Vegetable<br>Capsules</span></p>
      <div class="pattern" role="img" aria-label="Band of triangles fading from pale yellow through orange to red"></div>
    </div>
  </article>
  <article class="label label--hormone">
    <div class="label__cap"></div>
    <div class="label__body">
      <h2 class="product-name">Hormone Align</h2>
      <div class="rule rule--top"></div>
      <p class="claim">Supports Healthy<br>Hormone Levels*</p>
      <div class="rule rule--bottom"></div>
      <p class="badge">Dietary Supplement</p>
      <p class="count"><span class="count__number">60</span><span class="count__unit">Vegetable<br>Capsules</span></p>
      <div class="pattern" role="img" aria-label="Band of triangles fading from pale yellow to deep green"></div>
    </div>
  </article>
  <article class="label label--sugar">
    <div class="label__cap"></div>
    <div class="label__body">
      <h2 class="product-name">Blood Sugar Align</h2>
      <div class="rule rule--top"></div>
      <p class="claim">Supports Healthy Blood<br>Glucose Levels*</p>
      <div class="rule rule--bottom"></div>
      <p class="badge">Dietary Supplement</p>
      <p class="count"><span class="count__number">60</span><span class="count__unit">Vegetable<br>Capsules</span></p>
      <div class="pattern" role="img" aria-label="Band of triangles fading from pale yellow to bright blue"></div>
    </div>
  </article>
</main>
</body>
</html>
```